Hip Surgeon needs a web page re-design.

I have a web page to provide information about the diseases of the hip joint for the patients from my private practice since 2008. I need a re-design job for a fresh new look.
We have made a new logo and a new stationery design here in Marqueloft (please see the uploaded files) and I want to make my web page look-alike the new design concepts.
I like the color blue and tones of blue, matching my logo and stationery.
I don't like "busy" designs. It must be clean, elegant and ease to read. The final design should be "mobile friendly" if possible.
Please visit my website www.vilacorendasul.com.br to take a look and get some inspiration.

```html
<!DOCTYPE html>
<html lang="pt">
<head>
<meta charset="utf-8">
<title>Dr. Rafael M. Couto – Cirurgia do Quadril</title>
<link href="https://fonts.googleapis.com/css2?family=Quicksand:wght@500;600&family=Open+Sans:wght@400;600;700&display=swap" rel="stylesheet">
<style>
:root{
  --blue:#1a8fd3;
  --blue-light:#2db4ef;
  --blue-dark:#0c5f9e;
  --navy:#0a4b86;
  --footer:#0b4a84;
  --text:#555b61;
  --muted:#8a8f94;
  --line:#e3e6e9;
  --white:#fff;
}
*{box-sizing:border-box;margin:0;padding:0}
html,body{width:923px;height:1200px;overflow:hidden;background:var(--white)}
body{position:relative;font-family:"Open Sans",sans-serif;color:var(--text)}
.top-rule{position:absolute;left:0;top:0;width:923px;height:3px;background:var(--blue-light)}
.brand{position:absolute;left:68px;top:26px;display:flex;align-items:center;gap:10px}
.brand-dot{width:48px;height:48px;border-radius:50%;background:var(--blue)}
.brand-name{font-family:"Quicksand",sans-serif;font-weight:600;color:var(--blue);font-size:22px;line-height:24px}
.appointment{position:absolute;right:70px;top:32px;text-align:right;font-family:"Quicksand",sans-serif;color:var(--blue)}
.appointment small{display:block;font-size:12px;font-weight:600}
.appointment strong{display:block;font-size:22px;font-weight:500;margin-top:2px}
.nav{position:absolute;left:69px;top:96px;width:784px;height:40px;display:flex;background:linear-gradient(var(--blue-light),#0d9be0);border-radius:3px 3px 0 0}
.nav a{flex:auto;color:var(--white);text-decoration:none;font-size:10.5px;font-weight:700;display:flex;align-items:center;justify-content:center;border-right:1px solid rgba(255,255,255,.25)}
.nav a:last-child{border:0}
.hero{position:absolute;left:69px;top:136px;width:784px;height:309px;overflow:hidden;background:linear-gradient(180deg,#a8c6dc 0%,#cfdbe2 35%,#7f9a4e 60%,#3e5a23 100%)}
.hero-badge{position:absolute;left:502px;top:24px;width:258px;height:258px;border-radius:50%;background:rgba(22,128,196,.88);color:var(--white);text-align:center;padding-top:74px}
.hero-badge h2{font-family:"Quicksand",sans-serif;font-weight:500;font-size:24px}
.hero-badge h3{font-family:"Quicksand",sans-serif;font-weight:500;font-size:18px;margin-top:2px}
.hero-badge p{font-size:9.5px;line-height:15px;margin:8px 28px 0}
.dots{display:flex;justify-content:center;gap:4px;margin-top:12px}
.dots i{width:8px;height:8px;border-radius:50%;background:rgba(255,255,255,.45)}
.dots i:first-child{background:var(--white)}
.features{position:absolute;left:96px;top:474px;width:760px;display:flex}
.feature{display:flex;gap:12px;width:256px}
.feature-icon{width:52px;height:60px;flex:none}
.feature h4{font-family:"Quicksand",sans-serif;font-weight:500;color:var(--blue);font-size:16px;margin-bottom:5px}
.feature p{font-size:10px;line-height:17px;color:var(--muted)}
.divider{position:absolute;left:70px;top:584px;width:784px;height:1px;background:var(--line)}
.bio{position:absolute;left:71px;top:626px;width:545px}
.bio h1{font-family:"Quicksand",sans-serif;font-weight:500;color:var(--blue);font-size:22px;margin-bottom:12px}
.bio .lead{font-size:12px;line-height:19px;margin-bottom:8px}
.bio p{font-size:10px;line-height:18.5px}
.portrait{position:absolute;left:686px;top:620px;width:133px;height:150px;border:1px solid #d8dcdf;padding:5px}
.portrait div{width:100%;height:100%;background:linear-gradient(#c9b9a3,#e9eaec 55%,#f4f5f6)}
.cards{position:absolute;left:71px;top:814px;display:flex;gap:37px}
.card{width:238px}
.card h5{font-family:"Quicksand",sans-serif;font-weight:500;color:var(--blue);font-size:16px;margin-bottom:9px;padding-left:3px}
.card-img{height:96px;border-radius:2px}
.card-img.hand{background:linear-gradient(135deg,#7d93b8,#e9c9ba 45%,#d9b3a3)}
.card-img.stretch{background:linear-gradient(135deg,#e7e9ea,#e5c6b6 55%,#2a3a5a)}
.card h6{font-size:12px;font-weight:400;color:#333;margin:12px 2px 5px}
.card p{font-size:9.5px;line-height:18.5px;color:var(--muted);padding-left:2px}
.btn{display:inline-block;margin-top:8px;width:96px;height:29px;line-height:29px;text-align:center;border-radius:3px;background:linear-gradient(var(--blue-dark),#0a3f6f);color:var(--white);font-size:10.5px;font-weight:700;letter-spacing:-.2px}
.booking{position:absolute;left:638px;top:788px;width:217px;height:179px;border-radius:6px;background:linear-gradient(#3cb0e6,#1a86cc 45%,#0d67b0);color:var(--white);padding:16px 0 0 24px}
.booking h5{font-family:"Quicksand",sans-serif;font-weight:600;font-size:14px;margin-bottom:18px}
.booking li{list-style:none;font-family:"Quicksand",sans-serif;font-weight:500;font-size:11px;line-height:21.5px;padding-left:10px;position:relative}
.booking li::before{content:"";position:absolute;left:0;top:8px;border:3px solid transparent;border-left:4px solid rgba(255,255,255,.8)}
.video{position:absolute;left:638px;top:982px;width:217px;height:64px;border-radius:6px;background:linear-gradient(#2a9ede,#0d63ab);color:var(--white);padding:13px 19px}
.video h5{font-family:"Quicksand",sans-serif;font-weight:500;font-size:16px}
.video p{font-size:10px;margin-top:2px}
.footer{position:absolute;left:0;top:1085px;width:923px;height:115px;background:var(--footer);color:var(--white)}
.footer-nav{position:absolute;left:72px;top:29px;font-family:"Quicksand",sans-serif;font-weight:600;font-size:12.5px;word-spacing:1px}
.copy{position:absolute;left:72px;top:57px;font-size:9.5px}
.address{position:absolute;right:77px;top:31px;text-align:right;font-size:10.5px;line-height:17px}
</style>
</head>
<body>
<div class="top-rule"></div>

<header>
  <div class="brand">
    <span class="brand-dot"></span>
    <div class="brand-name">Dr. Rafael M. Couto<br>Cirurgia do Quadril</div>
  </div>
  <div class="appointment"><small>Make an Appointment</small><strong>416.555.0184</strong></div>
</header>

<nav class="nav">
  <a>Home</a><a>Saiba Mais</a><a>Curriculam Lattes</a><a>Links</a><a>Downloads</a><a>Atualidades</a><a>Contatc Us</a>
</nav>

<section class="hero">
  <div role="img" aria-label="Photo of an older couple cycling outdoors among trees" style="position:absolute;inset:0"></div>
  <div class="hero-badge">
    <h2>Dr. Rafael M. Couto</h2>
    <h3>Circurgia do Quadril</h3>
    <p>Cum sociis natoque penatibus et magnis dis parturient montes nascetur ridiculus mus In iaculis facilisis massa</p>
    <div class="dots"><i></i><i></i><i></i><i></i></div>
  </div>
</section>

<section class="features">
  <div class="feature">
    <div class="feature-icon" role="img" aria-label="Doctor icon" style="background:linear-gradient(#9aa0a6,#8a9096);border-radius:20px 20px 4px 4px;width:46px"></div>
    <div><h4>Meet Our Doctors</h4><p>Vestibulum ligula augue bibendum accumsan vestibulum ut commodo a mi Morbi Curabitur iaculis</p></div>
  </div>
  <div class="feature">
    <div class="feature-icon" role="img" aria-label="Running person icon" style="background:#8a9096;border-radius:50% 50% 10px 10px;width:36px;margin:0 8px 0 4px"></div>
    <div><h4>Services Provide</h4><p>Vestibulum ligula augue bibendum accumsan vestibulum ut commodo a mi Morbi Curabitur iaculis</p></div>
  </div>
  <div class="feature">
    <svg class="feature-icon" viewBox="0 0 58 60" aria-hidden="true">
      <path d="M8 36 L2 56 L56 56 L50 36" fill="none" stroke="#8a9096" stroke-width="2"/>
      <path d="M24 4a12 12 0 0 1 12 12c0 9-12 24-12 24S12 25 12 16A12 12 0 0 1 24 4z" fill="#8a9096"/>
      <circle cx="24" cy="16" r="5" fill="#fff"/>
    </svg>
    <div><h4>Our Location</h4><p>Vestibulum ligula augue bibendum accumsan vestibulum ut commodo a mi Morbi Curabitur iaculis</p></div>
  </div>
</section>

<div class="divider"></div>

<section class="bio">
  <h1>Dr. Rafael Moreira Couto</h1>
  <p class="lead">Donec scelerisque leo ac risus Praesent sit amet est In dictum dolor eu dictum porttitor enim felis viverra mi eget luctus massa purus quis odio Etiam nulla massa</p>
  <p>Aliquam nec erat at purus cursus interdum Vestibulum ligula augue bibendum accumsan vestibulum ut commodo a mi Morbi ornare gravida elit Integer congue augue et malesuada iaculis ipsum dui aliquet felis at cursus magna nisl nec elit Praesent elementum elit at tellus nec ultricies sit amet porttitor mattis enim</p>
</section>
<div class="portrait"><div role="img" aria-label="Portrait photo of the surgeon in a white coat"></div></div>

<section class="cards">
  <article class="card">
    <h5>PRODUCTS</h5>
    <div class="card-img hand" role="img" aria-label="Photo of hands examining a patient's hip"></div>
    <h6>Nunc tempus felis vitae urna</h6>
    <p>Vivamus porttitor g puttrus nisi eleifend libero a tempus libero lectus feugiat felis Morbi diam</p>
    <a class="btn">READ MORE</a>
  </article>
  <article class="card">
    <h5>SAIBA MAIS</h5>
    <div class="card-img stretch" role="img" aria-label="Photo of a patient doing a hip stretch with a therapist"></div>
    <h6>Curabitur iaculis tempus eros</h6>
    <p>Vivamus porttitor g puttrus nisi eleifend libero a tempus libero lectus feugiat felis Morbi diam</p>
    <a class="btn">READ MORE</a>
  </article>
</section>

<aside class="booking">
  <h5>AGENDE SUA CONSULTA</h5>
  <ul><li>Injuries &amp; Conditions</li><li>Sports Activities</li><li>Work Activities</li><li>Injury Care</li><li>Pain Care</li></ul>
</aside>
<aside class="video"><h5>Video Channel</h5><p>Please sign up here for latest offers</p></aside>

<footer class="footer">
  <div class="footer-nav">HOME &nbsp;|&nbsp; ABOUT US &nbsp;|&nbsp; SERVICES &nbsp;|&nbsp; BLOG &nbsp;|&nbsp; TESTIMONIALS &nbsp;|&nbsp; TREATMENT &nbsp;|&nbsp; CONTACT US</div>
  <div class="copy">© 2014 Company Name.&nbsp; All right reserved.&nbsp; Term of Use</div>
  <div class="address">418 Larkfield Road<br>Westbrook, Ontario, Canada. L4N 2K7<br>Phone: (416) 555-0184</div>
</footer>
</body>
</html>
```